Welcome signage for KJT Software Consulting Company

I need Welcome signage for KJT Consulting company Office Window. We are a Computer software company that offers software Implementation and Training for our Customers windows size 1. 900mm high 750mm wide. size 2. 1000mm high 700 wide.
Please review our website for branding and ideas.
The poster needs to contain our logo, website www.kjtconsulting-example.net.au and ph number 1300 46 81 07 , and the strap line... Empowering businesses with software choice.
Updates

Hi I'm really keen to find the perfect design. I had decided on one however the designer was dismissed from the group by admin so here I go again. Please read the briefs already in the information and hopefully I am excited by new submissions when I arrive to work on Monday xxx Thanks heaps fellow Designers x

```html
<!DOCTYPE html>
<html lang="en">
<head>
<meta charset="utf-8">
<title>KJT Consulting — Welcome Signage</title>
<link href="https://fonts.googleapis.com/css2?family=Oswald:wght@500&family=Questrial&family=Open+Sans:wght@700&display=swap" rel="stylesheet">
<style>
  :root {
    --stage: #f4f4f4;
    --paper: #ffffff;
    --paper-shade: #eeeeee;
    --ink: #58585a;
    --ink-dark: #4a4a4c;
    --orange: #ef8510;
    --orange-deep: #e8650f;
    --amber: #f6a81a;
  }
  html, body { margin: 0; padding: 0; overflow: hidden; }
  body {
    width: 1200px; height: 1000px;
    background: var(--stage);
    position: relative;
  }
  .poster {
    position: absolute; left: 92px; top: 72px;
    width: 1013px; height: 843px;
    background: linear-gradient(160deg, var(--paper) 0%, var(--paper) 55%, var(--paper-shade) 100%);
    overflow: hidden;
  }
  .poster-art { position: absolute; inset: 0; }
  .brand {
    position: absolute; left: 33px; top: 125px;
    display: flex; align-items: center; gap: 14px;
  }
  .brand-name {
    font-family: "Questrial", sans-serif;
    font-size: 108px; line-height: 1; letter-spacing: 6px;
    color: var(--ink);
  }
  .brand-dot {
    width: 56px; height: 56px; border-radius: 50%;
    background: var(--orange);
  }
  .strapline {
    position: absolute; left: 32px; top: 294px;
    margin: 0;
    font-family: "Oswald", sans-serif; font-weight: 500;
    font-size: 60px; line-height: 66px;
    text-transform: uppercase; color: var(--ink);
    letter-spacing: -1.2px;
  }
  .strapline .accent { color: var(--orange); }
  .strapline-rule {
    position: absolute; left: 35px; top: 494px;
    width: 421px; height: 4px; background: var(--orange);
  }
  .contact-phone {
    position: absolute; left: 35px; top: 580px;
    display: flex; align-items: center;
  }
  .phone-badge {
    width: 84px; height: 84px; border-radius: 50%;
    background: var(--ink-dark);
    border: 3px solid var(--paper);
    box-sizing: border-box;
    display: flex; align-items: center; justify-content: center;
    position: relative; z-index: 1;
  }
  .phone-number {
    margin-left: -22px;
    height: 56px; padding: 0 22px 0 40px;
    background: var(--ink-dark); border-radius: 0 12px 12px 0;
    display: flex; align-items: center;
    font-family: "Oswald", sans-serif; font-weight: 500;
    font-size: 40px; color: #fff; letter-spacing: 0;
  }
  .contact-web {
    position: absolute; left: 134px; top: 656px;
    font-family: "Open Sans", sans-serif; font-weight: 700;
    font-size: 14px; color: var(--orange);
  }
</style>
</head>
<body>
  <main class="poster">
    <svg class="poster-art" viewBox="0 0 1013 843" width="1013" height="843">
      <defs>
        <linearGradient id="office-tones" x1="0" y1="0" x2="1" y2="1">
          <stop offset="0" stop-color="#e4e9ec"/>
          <stop offset="0.45" stop-color="#b9c3cc"/>
          <stop offset="0.75" stop-color="#4a5a78"/>
          <stop offset="1" stop-color="#1d2230"/>
        </linearGradient>
      </defs>
      <polygon class="team-photo" role="img"
        aria-label="Photo: a team of colleagues gathered around a meeting table with a tablet and laptop in a bright office"
        points="348,0 1013,0 1013,843 653,843" fill="url(#office-tones)"/>
      <polygon class="band-amber" points="337,0 352,0 680,843 660,843" fill="var(--amber)" opacity="0.85"/>
      <polygon class="band-orange" points="323,0 348,0 666,843 653,843" fill="var(--orange)" opacity="0.9"/>
      <polygon class="corner-wedge-back" points="876,0 1013,0 1013,268" fill="var(--orange-deep)"/>
      <polygon class="corner-wedge-front" points="930,0 1013,0 1013,160" fill="var(--orange)"/>
      <polygon class="base-wedge" points="318,843 522,494 653,843" fill="var(--orange)"/>
      <polygon class="base-wedge-deep" points="522,494 548,484 678,843 653,843" fill="var(--orange-deep)"/>
    </svg>

    <div class="brand">
      <span class="brand-name">KJT</span>
      <span class="brand-dot"></span>
    </div>

    <h1 class="strapline">Empowering<br><span class="accent">Businesses</span> with<br>Software Choice.</h1>
    <div class="strapline-rule"></div>

    <div class="contact-phone">
      <div class="phone-badge">
        <svg width="36" height="36" viewBox="0 0 24 24" aria-hidden="true">
          <path fill="#fff" d="M6.6 10.8c1.4 2.8 3.8 5.1 6.6 6.6l2.2-2.2c.3-.3.7-.4 1-.2 1.1.4 2.3.6 3.6.6.6 0 1 .4 1 1V20c0 .6-.4 1-1 1C10.6 21 3 13.4 3 4c0-.6.4-1 1-1h3.5c.6 0 1 .4 1 1 0 1.3.2 2.5.6 3.6.1.3 0 .7-.2 1l-2.3 2.2z"/>
        </svg>
      </div>
      <div class="phone-number">1300 46 81 07</div>
    </div>
    <div class="contact-web">www.kjtconsulting-example.net.au</div>
  </main>
</body>
</html>
```